Cute Cow with Camera Card

The client is a cow crazy photographer specialising in weddings.
Her website is www.pelvantra.com.au.

TEXT
Delia Furness
0402 586 174

www.pelvantra.com.au
dfurness@brelkon.net.au

IMPORTANT NOTE
Card will be a die cutout
350gsm matt paper, one sided
maximum Design size, 54mmx86mm

Target Market(s)

Brides-to-be getting married, must impress wedding suppliers

Industry/Entity Type

Camera

Requirements
Must have
• Corporate colours are red, black & white

(see old design for TIPPA LUNE logo)

COW SPECS
Must be original animation
cute cow
fat cow
big eyes
cow using a camera (either sitting and two hoves holder camera to face or around neck like a bell would be)
design a female cow (could use female eye latches but be mindful of cutout)

suggestions
Would prefer a front-on design (for example cow sitting, exposing a big face, round tummy and short stubby hoves) not necessarily side view

Should not have
• MUST NOT HAVE:
any reference to beef, meat, cow branding

```html
<!DOCTYPE html>
<html lang="en">
<head>
<meta charset="utf-8">
<title>Delia Furness – Wedding Photographer Business Card</title>
<link rel="stylesheet" href="https://fonts.googleapis.com/css2?family=Cabin:wght@400&display=swap">
<style>
  :root {
    --backdrop: #98a1a7;
    --card: #ffffff;
    --brand-red: #c8001e;
    --text-light: #ffffff;
    --cow-white: #f7f3f2;
    --cow-pink: #f6c4dc;
    --cow-grey: #d9d6d6;
  }
  * { margin: 0; padding: 0; box-sizing: border-box; }
  html, body {
    width: 1200px;
    height: 900px;
    overflow: hidden;
    background: var(--backdrop);
  }
  .business-card {
    position: absolute;
    left: 93px;
    top: 132px;
    width: 1015px;
    height: 638px;
    background: var(--card);
    border-radius: 40px;
  }
  .speech-bubble {
    position: absolute;
    left: 0;
    top: 0;
    width: 1015px;
    height: 638px;
  }
  .contact-block {
    position: absolute;
    left: 139px;
    top: 142px;
    color: var(--text-light);
    font-family: "Cabin", "Gill Sans", sans-serif;
    font-weight: 400;
  }
  .contact-name {
    font-size: 36px;
    line-height: 50px;
  }
  .contact-role {
    font-size: 31px;
    line-height: 45px;
    margin-top: 3px;
  }
  .contact-details {
    list-style: none;
    font-size: 30px;
    line-height: 45px;
    margin-top: 26px;
  }
  .cow-illustration {
    position: absolute;
    left: 585px;
    top: 82px;
    width: 395px;
    height: 478px;
    border-radius: 46% 46% 40% 40%;
    background: radial-gradient(ellipse at 45% 40%, var(--cow-white) 0%, var(--cow-grey) 70%, var(--cow-pink) 100%);
  }
</style>
</head>
<body>
  <main class="business-card">
    <svg class="speech-bubble" viewBox="0 0 1015 638" aria-hidden="true">
      <circle cx="280" cy="318" r="239" fill="var(--brand-red)"/>
      <polygon points="500,262 575,276 508,318" fill="var(--brand-red)"/>
    </svg>

    <section class="contact-block">
      <h1 class="contact-name">Delia<br>Furness</h1>
      <p class="contact-role">wedding<br>photographer</p>
      <ul class="contact-details">
        <li class="contact-phone">tel: 0402 586 174</li>
        <li class="contact-email">dfurness@brelkon.net.au</li>
        <li class="contact-web">pelvantra.com.au</li>
      </ul>
    </section>

    <div class="cow-illustration" role="img" aria-label="Cartoon illustration of a cute, round, black-and-white spotted female cow standing front-on and holding a camera"></div>
  </main>
</body>
</html>
```